Business Cards

We were billed for this because the project timed out. Please give me another designed to open this back up. I was not happy with the last designs (that I was charged for).
we are also using the logo with Refreshing Waters One Visit at a Time
Also want to utilize Where Healthy Water is our Commitment.

Contact Information for Business Card

Marlowe Stone Group Inc

```html
<!DOCTYPE html>
<html lang="en">
<head>
<meta charset="utf-8">
<title>Marlowe Stone Group – Business Cards</title>
<link rel="stylesheet" href="https://fonts.googleapis.com/css2?family=Roboto:wght@400;500;700&display=swap">
<style>
  :root {
    --stage: #d1d2d4;
    --paper: #ffffff;
    --brand-blue: #146ab2;
    --back-blue: #1667b0;
    --swoosh: #3ea3dc;
    --ink: #4a4a4a;
    --tagline-ink: #555a60;
    --on-blue: #ffffff;
    --on-blue-soft: #c9d9ea;
  }
  * { box-sizing: border-box; margin: 0; padding: 0; }
  html, body { width: 1200px; height: 1000px; overflow: hidden; }
  body {
    background: var(--stage);
    font-family: "Roboto", Arial, sans-serif;
    position: relative;
  }
  .card {
    position: absolute;
    width: 545px;
    height: 312px;
    overflow: hidden;
    box-shadow: 0 1px 3px rgba(0,0,0,0.18);
  }
  .card-front { left: 327px; top: 177px; background: var(--paper); }
  .card-back  { left: 328px; top: 511px; background: var(--back-blue); }

  .front-wave { position: absolute; inset: 0; }

  .brand {
    position: absolute;
    left: 0; right: 0;
    display: flex;
    flex-direction: column;
    align-items: center;
  }
  .brand-row { display: flex; align-items: center; gap: 10px; }
  .brand-square { width: 16px; height: 16px; background: var(--brand-blue); }
  .brand-name {
    font-weight: 700;
    text-transform: uppercase;
  }
  .brand-tagline {
    font-weight: 500;
    text-transform: uppercase;
  }
  .card-front .brand { top: 72px; }
  .card-front .brand-name { font-size: 19px; letter-spacing: 2.2px; color: var(--ink); }
  .card-front .brand-tagline { font-size: 9px; letter-spacing: 2.6px; color: var(--tagline-ink); margin-top: 2px; }

  .card-back .brand { top: 162px; }
  .card-back .brand-square { background: var(--on-blue); }
  .card-back .brand-name { font-size: 21px; letter-spacing: 3px; color: var(--on-blue); }
  .card-back .brand-tagline { font-size: 10px; letter-spacing: 3px; color: var(--on-blue-soft); margin-top: 3px; }

  .contact {
    position: absolute;
    left: 44px;
    top: 182px;
    color: var(--on-blue);
    font-size: 13px;
    line-height: 16px;
  }
  .address { margin-bottom: 9px; }
  .contact-line { display: flex; align-items: center; gap: 5px; height: 18px; }
  .contact-line svg { width: 12px; height: 12px; flex: none; }

  .person {
    position: absolute;
    right: 45px;
    top: 237px;
    text-align: right;
    color: var(--on-blue);
  }
  .person-name { font-size: 14.5px; font-weight: 700; letter-spacing: 0.3px; }
  .person-title { font-size: 14px; margin-top: 3px; }
</style>
</head>
<body>

<section class="card card-front">
  <svg class="front-wave" viewBox="0 0 545 312" width="545" height="312">
    <path d="M0 163 C 100 118, 200 140, 290 180 C 370 212, 460 178, 545 141 L545 312 L0 312 Z" fill="var(--brand-blue)"/>
    <path d="M24 142 C 70 125, 130 112, 200 130 C 260 148, 300 185, 360 182 C 430 180, 480 160, 520 144 C 470 170, 420 190, 350 188 C 290 186, 250 150, 190 136 C 130 122, 70 130, 24 142 Z" fill="var(--swoosh)"/>
  </svg>

  <div class="brand">
    <div class="brand-row">
      <span class="brand-square"></span>
      <span class="brand-name">Marlowe Stone Group</span>
    </div>
    <span class="brand-tagline">Refreshing Waters One Visit at a Time</span>
  </div>

  <div class="contact">
    <p class="address">48 Harbor Lane, Suite 5<br>Milton, MA 02186</p>
    <p class="contact-line">
      <svg viewBox="0 0 24 24"><path fill="currentColor" d="M6.6 10.8a15.1 15.1 0 0 0 6.6 6.6l2.2-2.2a1 1 0 0 1 1-.25 11.4 11.4 0 0 0 3.6.57 1 1 0 0 1 1 1V20a1 1 0 0 1-1 1A17 17 0 0 1 3 4a1 1 0 0 1 1-1h3.5a1 1 0 0 1 1 1c0 1.25.2 2.45.57 3.57a1 1 0 0 1-.25 1z"/></svg>
      (555) 014-2290
    </p>
    <p class="contact-line">
      <svg viewBox="0 0 24 24"><rect x="2" y="5" width="20" height="14" fill="none" stroke="currentColor" stroke-width="2.4"/><path d="M2 5l10 8 10-8" fill="none" stroke="currentColor" stroke-width="2.4"/></svg>
      hello@marlowestonegroup.com
    </p>
    <p class="contact-line">
      <svg viewBox="0 0 24 24"><g fill="none" stroke="currentColor" stroke-width="2"><circle cx="12" cy="12" r="10"/><ellipse cx="12" cy="12" rx="4.5" ry="10"/><path d="M2 12h20M4 7h16M4 17h16"/></g></svg>
      www.marlowestonegroup.com
    </p>
  </div>

  <div class="person">
    <p class="person-name">DANA R. WHITFIELD</p>
    <p class="person-title">Founder &amp; CEO</p>
  </div>
</section>

<section class="card card-back">
  <div class="brand">
    <div class="brand-row">
      <span class="brand-square"></span>
      <span class="brand-name">Marlowe Stone Group</span>
    </div>
    <span class="brand-tagline">Refreshing Waters One Visit at a Time</span>
  </div>
</section>

</body>
</html>
```